Design new modern Business Cards

I'm looking for a new modern business card & Stationery design.
We are an Architectural Lighting business that imports products from Europe and Australasia.
see our website for further information: [url removed, login to view]
- Card is to be double sided.
- Design is to be based on 4 colours: White, Green, Grey and Black ( Can provide Colour Number)
- successful design is to be supplied in Indesign format for future updates.

```html
<!DOCTYPE html>
<html lang="en">
<head>
<meta charset="utf-8">
<title>Lumenvale Business Card</title>
<link href="https://fonts.googleapis.com/css2?family=Josefin+Sans:wght@300;400;600&display=swap" rel="stylesheet">
<style>
  :root {
    --green: #8cb43c;
    --green-deep: #6f9330;
    --green-pale: #d9e6bd;
    --grey: #6e6e6e;
    --grey-light: #9a9a9a;
    --white: #ffffff;
    --backdrop: #ececec;
    --ink: #3a3a3a;
  }
  * { margin: 0; padding: 0; box-sizing: border-box; }
  html, body { width: 1200px; height: 797px; overflow: hidden; }
  body {
    background: var(--backdrop);
    font-family: "Josefin Sans", "Helvetica Neue", Arial, sans-serif;
    position: relative;
  }
  .card {
    position: absolute;
    width: 520px;
    height: 297px;
    background: var(--white);
    box-shadow: 0 6px 18px rgba(0,0,0,0.12);
    overflow: hidden;
  }
  .card--contact { left: 50px; top: 250px; }
  .card--brand { left: 630px; top: 250px; }

  /* contact side */
  .beam { position: absolute; inset: 0; }
  .brand-band {
    position: absolute;
    left: 0; top: 150px;
    width: 185px; height: 38px;
    background: var(--green);
    display: flex; flex-direction: column; justify-content: center;
    padding-left: 16px;
    color: var(--white);
  }
  .brand-band__name { font-size: 22px; font-weight: 300; letter-spacing: 1px; line-height: 1; }
  .brand-band__tag { font-size: 5.5px; letter-spacing: 0.8px; margin-top: 2px; }
  .brand-rule {
    position: absolute; left: 185px; top: 186px;
    width: 335px; height: 2px; background: var(--green);
  }
  .holder { position: absolute; left: 290px; top: 30px; width: 200px; }
  .holder__name { color: var(--green-deep); font-size: 17px; font-weight: 400; letter-spacing: 0.5px; }
  .holder__role {
    font-size: 9px; font-style: italic; color: var(--green-deep);
    text-align: right; padding-right: 40px; border-top: 1px solid var(--grey-light);
    margin-top: 3px; padding-top: 2px;
  }
  .contacts { position: absolute; left: 260px; top: 80px; list-style: none; }
  .contacts li {
    display: flex; align-items: center; gap: 12px;
    height: 24px; font-size: 9px; color: var(--ink);
  }
  .contacts svg { width: 13px; height: 13px; flex: none; }

  /* brand side */
  .brand-top { position: absolute; left: 0; top: 0; width: 100%; height: 148px; background: var(--green); }
  .brand-mark {
    position: absolute; left: 0; top: 118px; width: 100%;
    text-align: center; color: var(--grey);
  }
  .brand-mark__name { font-size: 50px; font-weight: 300; letter-spacing: 2px; line-height: 1; }
  .brand-mark__tag { font-size: 8px; letter-spacing: 1.5px; margin-top: 4px; padding-left: 60px; }
</style>
</head>
<body>
  <section class="card card--contact">
    <svg class="beam" viewBox="0 0 520 297" aria-hidden="true">
      <polygon points="250,0 520,0 520,205 185,188 185,150" fill="var(--green-pale)"/>
    </svg>
    <div class="brand-band">
      <span class="brand-band__name">LUMENVALE</span>
      <span class="brand-band__tag">ARCHITECTURAL • BESPOKE LIGHTING</span>
    </div>
    <div class="brand-rule"></div>
    <div class="holder">
      <p class="holder__name">MR. YOUR NAME</p>
      <p class="holder__role">Founder</p>
    </div>
    <ul class="contacts">
      <li>
        <svg viewBox="0 0 16 16"><rect x="1" y="3" width="14" height="10" fill="var(--grey)"/><polyline points="1,3 8,9 15,3" fill="none" stroke="var(--white)" stroke-width="1.2"/></svg>
        <span>hello@lumenvale.com</span>
      </li>
      <li>
        <svg viewBox="0 0 16 16"><rect x="4" y="1" width="8" height="14" rx="1.5" fill="none" stroke="var(--grey)" stroke-width="1.4"/><circle cx="8" cy="12.5" r="0.9" fill="var(--grey)"/></svg>
        <span>55 3810 7742</span>
      </li>
      <li>
        <svg viewBox="0 0 16 16" fill="none" stroke="var(--grey)" stroke-width="1.2"><circle cx="8" cy="8" r="6.5"/><ellipse cx="8" cy="8" rx="3" ry="6.5"/><line x1="1.5" y1="8" x2="14.5" y2="8"/></svg>
        <span>www.lumenvale.com</span>
      </li>
      <li>
        <svg viewBox="0 0 16 16"><path d="M8 1a4.5 4.5 0 0 0-4.5 4.5C3.5 9 8 14 8 14s4.5-5 4.5-8.5A4.5 4.5 0 0 0 8 1z" fill="var(--grey)"/><circle cx="8" cy="5.5" r="1.6" fill="var(--white)"/></svg>
        <span>Calle Olmo #42 Esq. Norte Col.<br>Jardines Altos</span>
      </li>
    </ul>
  </section>

  <section class="card card--brand">
    <div class="brand-top"></div>
    <div class="brand-mark">
      <p class="brand-mark__name">LUMENVALE</p>
      <p class="brand-mark__tag">ARCHITECTURAL • BESPOKE LIGHTING</p>
    </div>
  </section>
</body>
</html>
```